Webdesign für Kanal Vertrieb
Zielgruppe
Die lotte & brandt Media Marketing GmbH beschäftigt sich mit der Entwicklung, Vermarktung und dem Vertrieb von Medialeistungen aus den Bereichen Print, TV, Radio, Internet (Digital) und Events. Weiterhin erstellt das Unternehmen Kommunikation- und Marketingkonzepte sowie die komplette Realisierung von Events und TV-Produktionen. Im Weiteren werden auch branchenverwandten Anwendungen und Bereiche abgedeckt, die den Unternehmenszielen dienen. Das Unternehmen betreut, vermittelt und vermarktet im weiteren Prominente, Kunstler und Moderatoren.
Die Zielgruppe ist B2B
Unsere Seite ist aktuell nun 2 Jahre alt und wir benötigen ein frisches Re-Design
Das Design soll zum Style des Logos passen, es soll elegant und professionelle hervorgehoben werden.
Die jetzige Seite findet mal unter www.lotte-brandt.de
Aufgabenstellung
Das Design soll frisch und elegant wirken, sowie einen professionellen Eindruck für eine Media Agentur machen. Das ganze soll dann im Anschluss in Word Press integrier bar sein und auch dort gepflegt werden.

```html
<!DOCTYPE html>
<html lang="de">
<head>
<meta charset="utf-8">
<title>lotte &amp; brandt – Kanal Vertrieb</title>
<link rel="stylesheet" href="https://fonts.googleapis.com/css2?family=Poppins:wght@300;400;500;600&display=swap">
<style>
:root{
  --black:#0b0b0c;
  --red:#dc231e;
  --red-dark:#b81d19;
  --ink:#26242f;
  --grey:#6f6f78;
  --soft:#f3f4f9;
  --white:#ffffff;
}
*{box-sizing:border-box;margin:0;padding:0}
html,body{width:1200px;height:3149px;overflow:hidden}
body{font-family:"Poppins",sans-serif;color:var(--ink);background:var(--white);position:relative}
.abs{position:absolute}
a{text-decoration:none;color:inherit}
.arrow{display:inline-block;vertical-align:middle;margin-left:10px}
.red-link{color:var(--red);font-size:12px;font-weight:400}
.brand{font-family:"Poppins",sans-serif;font-weight:500;font-size:20px;letter-spacing:.5px}
.brand small{display:block;font-size:7px;letter-spacing:4px;font-weight:400;margin-top:2px}

/* hero */
.hero{left:0;top:0;width:1200px;height:475px;background:var(--black);color:var(--white)}
.hero .brand{left:100px;top:18px}
.nav{right:100px;top:27px;display:flex;gap:28px;font-size:12px}
.hero h1{left:100px;top:144px;width:520px;font-size:39px;line-height:51px;font-weight:600}
.btn{display:inline-block;border-radius:22px;font-size:12px;text-align:center}
.hero .btn{left:100px;top:320px;width:170px;height:38px;line-height:38px;background:var(--red);color:var(--white)}
.hero-media{left:740px;top:90px;width:305px;height:330px;border-radius:6px;background:linear-gradient(160deg,#3a3a3e 0%,#1c1c1e 55%,#0b0b0c 100%)}

/* services */
.services{left:0;top:475px;width:1200px;height:413px;background:var(--soft)}
.services h2{left:100px;top:65px;font-size:33px;font-weight:500}
.services .intro{left:100px;top:115px;width:305px;font-size:9.5px;line-height:17.5px;color:var(--grey)}
.services .red-link{left:100px;top:199px}
.service{width:230px}
.service .num{display:inline-block;width:31px;height:31px;border-radius:4px;background:var(--black);color:var(--white);font-size:10px;text-align:center;line-height:31px;border-bottom:3px solid var(--red)}
.service h3{font-size:21px;font-weight:400;margin:12px 0 10px}
.service p{font-size:10px;line-height:17.5px;color:var(--grey)}

/* projects */
.projects-title{left:100px;top:967px;font-size:31px;font-weight:500}
.projects-all{right:100px;top:982px}
.card{overflow:hidden;color:var(--white)}
.card h3{font-size:22px;font-weight:500;line-height:25px}
.card .go{font-size:12px}
.card-big{left:100px;top:1047px;width:575px;height:374px}
.card-big .left{position:absolute;left:0;top:0;width:320px;height:374px;background:linear-gradient(180deg,#c82a25,#dd3a33)}
.card-big .right{position:absolute;left:320px;top:0;width:255px;height:374px;background:linear-gradient(180deg,#e8e3dc,#6f6f70 60%,#3a3c44)}
.card-big .txt{position:absolute;left:36px;top:254px}
.card-big .btn{margin-top:10px;width:114px;height:29px;line-height:29px;background:var(--white);color:var(--red)}
.card-small{left:695px;width:405px;height:177px}
.card-small .left{position:absolute;left:0;top:0;width:137px;height:100%}
.card-small .right{position:absolute;left:137px;top:0;width:268px;height:100%;background:linear-gradient(135deg,#e04540,#c9231f)}
.card-small .txt{position:absolute;left:161px;bottom:24px}
.card-small .go{margin-top:8px;display:block}

/* testimonial */
.quotes{left:100px;top:1543px;width:1000px;height:316px;background:var(--black);color:var(--white)}
.quotes h2{position:absolute;left:50px;top:105px;font-size:24px;font-weight:500;line-height:30px}
.quotes .sub{position:absolute;left:50px;top:176px;width:280px;font-size:10px;line-height:17.5px;color:#c9c9cf}
.quotes blockquote{position:absolute;left:425px;top:60px;width:460px;font-size:20px;line-height:30px}
.author{position:absolute;left:425px;top:220px;display:flex;align-items:center;gap:12px}
.author .avatar{width:32px;height:32px;border-radius:50%;background:#9a8a7e}
.author b{display:block;font-size:12px;font-weight:500}
.author span{font-size:7px}
.pager{position:absolute;right:40px;top:260px;display:flex;gap:8px}
.pager span{width:29px;height:29px;border-radius:50%;display:flex;align-items:center;justify-content:center}

/* team */
.team h2{left:100px;top:1954px;font-size:31px;font-weight:500;line-height:40px}
.team .intro{left:100px;top:2048px;width:470px;font-size:10px;line-height:17.5px;color:var(--grey)}
.job{top:2141px;width:320px;height:196px;background:var(--soft);padding:28px 30px}
.job h3{font-size:16px;font-weight:400;margin:14px 0 12px}
.job p{font-size:10px;line-height:17.5px;color:var(--grey);margin-bottom:10px}

/* call to action */
.cta{left:99px;top:2456px;width:1001px;height:316px;background:var(--red);color:var(--white)}
.cta h2{position:absolute;left:66px;top:50px;font-size:31px;font-weight:600;line-height:40px}
.cta p{position:absolute;left:66px;top:145px;width:490px;font-size:10px;line-height:17.5px}
.cta .btn{position:absolute;left:66px;top:227px;width:174px;height:40px;line-height:40px;background:var(--white);color:var(--red)}
.cta-photo{left:747px;top:2413px;width:316px;height:359px;background:linear-gradient(180deg,#5a4a40 0%,#d9c0ad 35%,#a9c3e0 60%,#8fb2d8 100%);border-radius:140px 140px 0 0}

/* footer */
.footer{left:0;top:2891px;width:1200px;height:198px;background:var(--black);color:var(--white)}
.footer .brand{position:absolute;left:100px;top:45px}
.footer .claim{position:absolute;left:100px;top:109px;font-size:10px;line-height:17.5px}
.fcol{position:absolute;top:43px;font-size:10px;line-height:17.5px;color:#c9c9cf}
.fcol h4{font-size:11px;font-weight:500;color:var(--white);margin-bottom:8px}
.bottom{left:0;top:3089px;width:1200px;height:60px;font-size:9px}
.bottom .legal{position:absolute;left:100px;top:27px}
.bottom .follow{position:absolute;right:100px;top:22px;display:flex;align-items:center;gap:8px}
.bottom .dot{width:14px;height:14px;border-radius:50%;background:var(--black)}
</style>
</head>
<body>

<header class="abs hero">
  <div class="abs brand">lotte &amp; brandt<small>KANAL VERTRIEB</small></div>
  <nav class="abs nav"><a>Agentur</a><a>Kompetenzen</a><a>Projekte</a><a>Karriere</a><a>Kontakt</a></nav>
  <h1 class="abs">Erzählen Sie uns Ihre Geschichte, wir erzählen sie weiter.</h1>
  <a class="abs btn">Unsere Geschichten</a>
  <div class="abs hero-media" role="img" aria-label="Aufgeklappter Laptop mit Sendergrafik von Nordlicht Kanal"></div>
</header>

<section class="abs services">
  <h2 class="abs">Was wir machen</h2>
  <p class="abs intro">Weit hinten, hinter den Wortbergen, fern der Länder Vokalien und Konsonantien leben die Blindtexte. Abgeschieden wohnen sie in Buchstabhausen an der Küste des Semantik, eines großen Sprachozeans.</p>
  <a class="abs red-link">Nehmen Sie Kontakt auf<svg class="arrow" width="16" height="8" viewBox="0 0 16 8"><path d="M0 4h14M11 1l3 3-3 3" stroke="#dc231e" fill="none"/></svg></a>
  <div class="abs service" style="left:525px;top:64px"><span class="num">01</span><h3>Internet</h3><p>Weit hinten, hinter den Wortbergen, fern der Länder Vokalien und Konsonantien leben die Blindtexte.</p></div>
  <div class="abs service" style="left:781px;top:64px"><span class="num">02</span><h3>Events</h3><p>Weit hinten, hinter den Wortbergen, fern der Länder Vokalien und Konsonantien leben die Blindtexte.</p></div>
  <div class="abs service" style="left:525px;top:219px"><span class="num">03</span><h3>TV Produktionen</h3><p>Weit hinten, hinter den Wortbergen, fern der Länder Vokalien und Konsonantien leben die Blindtexte.</p></div>
  <div class="abs service" style="left:781px;top:219px"><span class="num">04</span><h3>Print</h3><p>Weit hinten, hinter den Wortbergen, fern der Länder Vokalien und Konsonantien leben die Blindtexte.</p></div>
</section>

<h2 class="abs projects-title">Unsere Projekte</h2>
<a class="abs red-link projects-all" style="font-size:10px">Alle Projekte<svg class="arrow" width="16" height="8" viewBox="0 0 16 8"><path d="M0 4h14M11 1l3 3-3 3" stroke="#dc231e" fill="none"/></svg></a>

<article class="abs card card-big">
  <div class="left" role="img" aria-label="Fernsehkamera bei einem Dreh, rot eingefärbt"></div>
  <div class="right" role="img" aria-label="Interview mit einem Koch bei einer Abendveranstaltung"></div>
  <div class="txt"><h3>Mit Nordlicht Kanal<br>auf Mallorca</h3><a class="btn">Zum Projekt</a></div>
</article>

<article class="abs card card-small" style="top:1047px">
  <div class="left" role="img" aria-label="Zwei Männer bei einer Präsentation vor einer Messewand" style="background:linear-gradient(180deg,#f2f2f4,#9aa0ad)"></div>
  <div class="right" role="img" aria-label="Messestand im Hintergrund, rot eingefärbt"></div>
  <div class="txt"><h3>#weShare Europa</h3><a class="go">Zum Projekt<svg class="arrow" width="16" height="8" viewBox="0 0 16 8"><path d="M0 4h14M11 1l3 3-3 3" stroke="#fff" fill="none"/></svg></a></div>
</article>

<article class="abs card card-small" style="top:1245px;height:176px">
  <div class="left" role="img" aria-label="Stapel Fernsehzeitschriften" style="background:linear-gradient(135deg,#b9d6f1,#e9a23b 55%,#cf2a24)"></div>
  <div class="right" role="img" aria-label="Titelseiten von Programmzeitschriften, rot eingefärbt"></div>
  <div class="txt"><h3>Unser TV Journal</h3><a class="go">Zum Projekt<svg class="arrow" width="16" height="8" viewBox="0 0 16 8"><path d="M0 4h14M11 1l3 3-3 3" stroke="#fff" fill="none"/></svg></a></div>
</article>

<section class="abs quotes">
  <h2>Das sagen<br>unsere Kunden</h2>
  <p class="sub">Weit hinten, hinter den Wortbergen, fern der Länder Vokalien und Konsonantien leben die Blindtexte.</p>
  <blockquote>"Die beste Agentur, mit der wir bisher zusammengearbeitet haben. Sie verstehen unser Produkt und sind in der Lage, neue Funktionen mit einem großen Fokus hinzuzufügen."</blockquote>
  <div class="author"><div class="avatar" role="img" aria-label="Porträtfoto der Kundin"></div><div><b>Jana Beispiel</b><span>Nordlicht Kanal</span></div></div>
  <div class="pager">
    <span style="background:var(--red-dark)"><svg width="10" height="10" viewBox="0 0 10 10"><path d="M6.5 1.5 3 5l3.5 3.5" stroke="#fff" stroke-width="1.6" fill="none"/></svg></span>
    <span style="background:var(--red)"><svg width="10" height="10" viewBox="0 0 10 10"><path d="M3.5 1.5 7 5 3.5 8.5" stroke="#fff" stroke-width="1.6" fill="none"/></svg></span>
  </div>
</section>

<section class="team">
  <h2 class="abs">Werde ein Teil des<br>großartigen Teams</h2>
  <p class="abs intro">Das weiße Blatt Papier? Hab keine Angst. Denn hätte, könnte, würde geben wir keine Chance. Wir sind Profis und setzen unsere Ideen um. Und wenn jemand in der Sackgasse durchhängt, holen wir ihn wieder raus. Mit Methoden, Teamspirit und richtig gutem Kaffee</p>
  <div class="abs job" style="left:100px"><svg width="20" height="20" viewBox="0 0 20 20"><path d="M3 3l14 14M17 3 3 17" stroke="#dc231e" stroke-width="4"/></svg><h3>Mediengestalter (m/w/x)</h3><p>Weit hinten, hinter den Wortbergen, fern der Länder Vokalien und Konsonantien leben die Blindtexte.</p><a class="red-link">Jetzt bewerben<svg class="arrow" width="16" height="8" viewBox="0 0 16 8"><path d="M0 4h14M11 1l3 3-3 3" stroke="#dc231e" fill="none"/></svg></a></div>
  <div class="abs job" style="left:440px"><svg width="20" height="20" viewBox="0 0 20 20"><rect x="2" y="3" width="13" height="16" fill="#dc231e"/><path d="M5 8h7M5 11h7M5 14h5" stroke="#fff"/></svg><h3>Projektmanager (m/w/x)</h3><p>Weit hinten, hinter den Wortbergen, fern der Länder Vokalien und Konsonantien leben die Blindtexte.</p><a class="red-link">Jetzt bewerben<svg class="arrow" width="16" height="8" viewBox="0 0 16 8"><path d="M0 4h14M11 1l3 3-3 3" stroke="#dc231e" fill="none"/></svg></a></div>
  <div class="abs job" style="left:780px"><svg width="20" height="20" viewBox="0 0 20 20"><circle cx="10" cy="6" r="3" fill="#dc231e"/><circle cx="4" cy="8" r="2.3" fill="#dc231e"/><circle cx="16" cy="8" r="2.3" fill="#dc231e"/><path d="M5 17a5 5 0 0 1 10 0zM0 17a4 4 0 0 1 6-3.5M20 17a4 4 0 0 0-6-3.5" fill="#dc231e"/></svg><h3>Office Manager (m/w/x)</h3><p>Weit hinten, hinter den Wortbergen, fern der Länder Vokalien und Konsonantien leben die Blindtexte.</p><a class="red-link">Jetzt bewerben<svg class="arrow" width="16" height="8" viewBox="0 0 16 8"><path d="M0 4h14M11 1l3 3-3 3" stroke="#dc231e" fill="none"/></svg></a></div>
</section>

<section class="abs cta">
  <h2>Starten Sie jetzt Ihr<br>Projekt mit uns!</h2>
  <p>Wo gibt's denn sowas? In Lindhaven! Im Herzen des Seenlands!<br>Da, wo man nicht „drum herum redet"! Treten Sie mit uns in Kontakt und fordern Sie uns heraus! Schildern Sie einfach Ihre Wünsche und erhalten Sie umgehend Mediaanalysen und konkrete Vorschläge und Angebote.</p>
  <a class="btn">Zum Kontaktformular</a>
</section>
<div class="abs cta-photo" role="img" aria-label="Freigestelltes Porträt des Geschäftsführers im hellblauen Sakko"></div>

<footer class="abs footer">
  <div class="brand">lotte &amp; brandt<small>KANAL VERTRIEB</small></div>
  <p class="claim">Wo gibt's denn sowas?<br>In Lindhaven! Im Herzen des Seenlands!<br>Da, wo man nicht „drum herum redet"!</p>
  <div class="fcol" style="left:440px"><h4>Kompetenzen</h4>Internet<br>Events<br>TV Produktionen<br>Print</div>
  <div class="fcol" style="left:610px"><h4>Über uns</h4>Agentur<br>Jobs<br>Kontakt</div>
  <div class="fcol" style="left:780px"><h4>Kontakt</h4>Kontaktformular<br>Anfahrt<br>Newsletter</div>
  <div class="fcol" style="left:950px"><h4>lotte &amp; brandt</h4>
    <svg width="9" height="9" viewBox="0 0 10 10"><path d="M2 1l2 2-1 1.5a6 6 0 0 0 2.5 2.5L7 6l2 2-1.5 1.5C4 9 1 6 .5 2.5z" fill="#c9c9cf"/></svg> 0171 555 0123<br>
    <svg width="9" height="8" viewBox="0 0 10 8"><rect width="10" height="8" fill="#c9c9cf"/><path d="M0 0l5 4 5-4" stroke="#0b0b0c" fill="none"/></svg> info@lottebrandt.de</div>
</footer>

<div class="abs bottom">
  <div class="legal">Impressum | Datenschutz | AGB</div>
  <div class="follow">Folgen Sie uns auf <span class="dot"></span><span class="dot"></span><span class="dot"></span></div>
</div>

</body>
</html>
```